Window company.

Hello,

We are a small family business located in Madrid, Spain that works nationwide to fix, change or mount the windows of your home / premises.

The group of possible clients to whom the flyer is focused ranges from 30 to 65 years, families in general who want comfort at home and extra savings every year in heating.

It must include not only graphics and a striking aesthetic in accordance with the concepts of wanting to reach / transmit the final product to the customer to sell the product.

Details to also include:

-Brief history of the company and its foundation in 2006. It will be subsequently translated into Spanish so put in words what you consider necessary so that the client stays with the concept that we are professionals.

--Specialized in exterior aluminum and PVC carpentry.

-We move to your home for a first visit and we provide the budget totally free without any commitment.

- Also payment facilities; up to 3 times, without interest.

-Contact details of the company. (WhatsApp, email, phone and location)
Open: Mon - Friday 11,00am - 9pm
Saturday: 12,00am - 7pm
Sunday: Closed

Also as a suggestion, to decide on your own, graphics of types of window openings, if you consider that anything that is striking for the client so it wonr be yet another advertising flyer.

We are open to all kinds of ideas, all of them involving marketing branding.

We are open to any type of idea and we want to stand out, the construction world is tough and we have an idea to grow, taking into account that it must not only be beautiful but commercial to attract potential customers with all kinds of purchasing power.

Thank you.

```html
<!DOCTYPE html>
<html lang="es">
<head>
<meta charset="utf-8">
<title>Ventalia – Ahorre en calefacción</title>
<link rel="stylesheet" href="https://fonts.googleapis.com/css2?family=Oswald:wght@400;500;600&family=Open+Sans:wght@400;600;700&display=swap">
<style>
  :root {
    --red: #c8322b;
    --red-dark: #a8261f;
    --ink: #2f2f2f;
    --grey-text: #8c8c8c;
    --panel: #f0f0f0;
    --footer: #a3a3a3;
    --white: #ffffff;
  }
  * { margin: 0; padding: 0; box-sizing: border-box; }
  html, body { width: 848px; height: 1200px; overflow: hidden; background: var(--white); }
  .flyer { position: relative; width: 848px; height: 1200px; overflow: hidden; background: var(--white); font-family: "Open Sans", Arial, sans-serif; color: var(--ink); }

  .hero-photo { position: absolute; left: 0; top: 96px; width: 848px; height: 430px;
    background: linear-gradient(90deg, #ffffff 0%, #fbf6f0 32%, #ead6c0 55%, #d3b08f 78%, #b98f6c 100%); }
  .hero-frame { position: absolute; left: 0; top: 0; width: 848px; height: 530px; }

  .brand { position: absolute; left: 40px; top: 74px; display: flex; align-items: center; gap: 14px; }
  .brand-square { width: 30px; height: 30px; background: var(--red); }
  .brand-name { font-family: "Oswald", Arial, sans-serif; font-weight: 500; font-size: 40px; letter-spacing: 1px; color: var(--grey-text); line-height: 1; }

  .social { position: absolute; top: 39px; left: 594px; display: flex; gap: 28px; }
  .social span { width: 36px; height: 36px; border: 2px solid #bdbdbd; border-radius: 50%; }

  .headline { position: absolute; left: 36px; top: 176px; font-family: "Oswald", Arial, sans-serif; font-weight: 500; font-size: 46px; line-height: 1.03; color: var(--ink); text-transform: uppercase; }
  .offer-bar { position: absolute; left: 0; top: 362px; width: 412px; height: 54px; background: var(--red);
    clip-path: polygon(0 0, 100% 0, 94% 100%, 0 100%);
    font-family: "Oswald", Arial, sans-serif; font-size: 28px; color: var(--white); line-height: 54px; padding-left: 36px; }
  .quality { position: absolute; left: 36px; top: 428px; font-family: "Oswald", Arial, sans-serif; font-weight: 500; font-size: 28px; color: var(--ink); text-transform: uppercase; }

  .about { position: absolute; left: 0; top: 526px; width: 848px; height: 210px; background: var(--panel); }
  .about-col { position: absolute; top: 28px; }
  .about-col.left { left: 34px; width: 364px; }
  .about-col.right { left: 444px; width: 388px; }
  .about-divider { position: absolute; left: 423px; top: 24px; width: 1px; height: 160px; background: #c5c5c5; }
  .about h2 { font-family: "Oswald", Arial, sans-serif; font-weight: 500; font-size: 23px; color: var(--red); margin-bottom: 16px; }
  .about h3 { font-size: 15.5px; font-weight: 700; line-height: 1.3; text-transform: uppercase; margin-bottom: 10px; }
  .about p { font-size: 16.5px; line-height: 1.35; text-align: justify; }
  .payment-tag { position: absolute; left: 444px; top: 152px; width: 388px; height: 36px; background: var(--red); color: var(--white); font-size: 13.5px; font-weight: 700; line-height: 36px; text-align: center; }

  .services { position: absolute; left: 0; top: 762px; width: 848px; height: 244px;
    background: linear-gradient(180deg, #7d7d7d 0%, #8f8f8f 40%, #a7a7a7 100%);
    border-top: 4px solid var(--red); border-bottom: 4px solid var(--red); }
  .services-tab { position: absolute; left: 0; top: 736px; width: 300px; height: 42px; background: var(--red);
    clip-path: polygon(0 0, 100% 0, 94% 100%, 0 100%);
    font-family: "Oswald", Arial, sans-serif; font-size: 24px; color: var(--white); line-height: 42px; padding-left: 34px; }
  .service-list { position: absolute; top: 30px; list-style: none; }
  .service-list.left { left: 42px; }
  .service-list.right { left: 426px; }
  .service-list li { display: flex; align-items: center; height: 51px; font-family: "Oswald", Arial, sans-serif; font-size: 20px; color: var(--white); text-transform: uppercase; }
  .service-icon { width: 42px; height: 42px; margin-right: 22px; flex: none; }

  .hours { position: absolute; left: 0; top: 1038px; width: 848px; text-align: center; font-size: 17px; color: var(--ink); }

  .footer { position: absolute; left: 0; top: 1114px; width: 848px; height: 86px; background: var(--footer); color: var(--white); text-align: center; font-size: 17.5px; line-height: 1.35; padding-top: 28px; }
  .call-pill { position: absolute; left: 78px; top: 1093px; width: 683px; height: 42px; border-radius: 12px; background: var(--red);
    display: flex; align-items: center; justify-content: center; gap: 10px; color: var(--white); font-size: 18.5px; font-weight: 700; }
  .call-pill svg { width: 20px; height: 20px; }
</style>
</head>
<body>
<main class="flyer">

  <div class="hero-photo" role="img" aria-label="Fotografía de una familia sonriente sentada en casa, la niña sostiene un tejado de cartón sobre sus padres"></div>
  <svg class="hero-frame" viewBox="0 0 848 530" aria-hidden="true">
    <polygon points="0,0 848,0 848,94 0,172" fill="#ffffff"/>
    <line x1="0" y1="172" x2="848" y2="94" stroke="#c8322b" stroke-width="7"/>
  </svg>

  <div class="brand">
    <span class="brand-square"></span>
    <span class="brand-name">VENTALIA</span>
  </div>

  <div class="social" aria-hidden="true"><span></span><span></span><span></span><span></span></div>

  <h1 class="headline">Ahorre<br>todos los años<br>en calefacción</h1>
  <div class="offer-bar">Presupuestos sin compromiso</div>
  <div class="quality">Calidad garantizada !</div>

  <section class="about">
    <div class="about-col left">
      <h2>QUIENES SOMOS</h2>
      <p>Somos una empresa familiar con mas de 20 años de experiencia trabajando a nivel nacional arreglando, montando y cambiando ventanas, persianas, etc.</p>
    </div>
    <div class="about-divider"></div>
    <div class="about-col right">
      <h3>Especializados en carpintería de aluminio exterior y carpintería de PVC.</h3>
      <p>Nos trasladamos a su vivienda para una primera visita y le proporcionamos un presupuesto totalmente gratuito.</p>
    </div>
    <div class="payment-tag">FACILIDADES DE PAGO; HASTA 3 VECES SIN INTERESES</div>
  </section>

  <section class="services" role="img" aria-label="Fotografía en tonos grises de una casa unifamiliar con ventanas">
    <ul class="service-list left">
      <li><svg class="service-icon" viewBox="0 0 42 42"><rect x="1" y="1" width="40" height="40" rx="4" fill="#c8322b" stroke="#fff" stroke-width="2"/><path d="M11 22 L21 13 L31 22 M14 20 V30 H28 V20" fill="none" stroke="#fff" stroke-width="2.5"/></svg>Carpinteria de exterior</li>
      <li><svg class="service-icon" viewBox="0 0 42 42"><rect x="1" y="1" width="40" height="40" rx="4" fill="#c8322b" stroke="#fff" stroke-width="2"/><path d="M10 13 H32 V19 H10 Z M12 19 V31 M30 19 V31" fill="none" stroke="#fff" stroke-width="2.5"/></svg>Toldos</li>
      <li><svg class="service-icon" viewBox="0 0 42 42"><rect x="1" y="1" width="40" height="40" rx="4" fill="#c8322b" stroke="#fff" stroke-width="2"/><path d="M12 10 H30 V32 H12 Z M21 10 V32" fill="none" stroke="#fff" stroke-width="2.5"/></svg>Aluminio</li>
      <li><svg class="service-icon" viewBox="0 0 42 42"><rect x="1" y="1" width="40" height="40" rx="4" fill="#c8322b" stroke="#fff" stroke-width="2"/><path d="M11 11 H31 V31 H11 Z M21 11 V31 M11 21 H31" fill="none" stroke="#fff" stroke-width="2.5"/></svg>Doble acristalamiento</li>
    </ul>
    <ul class="service-list right">
      <li><svg class="service-icon" viewBox="0 0 42 42"><rect x="1" y="1" width="40" height="40" rx="4" fill="#c8322b" stroke="#fff" stroke-width="2"/><path d="M11 11 H31 V31 H11 Z M21 11 V31 M11 21 H31" fill="none" stroke="#fff" stroke-width="2.5"/></svg>PVC</li>
      <li><svg class="service-icon" viewBox="0 0 42 42"><rect x="1" y="1" width="40" height="40" rx="4" fill="#c8322b" stroke="#fff" stroke-width="2"/><path d="M11 11 H31 V31 H11 Z M16 11 V31 M21 11 V31 M26 11 V31 M11 16 H31 M11 21 H31 M11 26 H31" fill="none" stroke="#fff" stroke-width="1.5"/></svg>Mosquiteras</li>
      <li><svg class="service-icon" viewBox="0 0 42 42"><rect x="1" y="1" width="40" height="40" rx="4" fill="#c8322b" stroke="#fff" stroke-width="2"/><path d="M10 14 L26 10 L32 30 L16 32 Z" fill="none" stroke="#fff" stroke-width="2.5"/></svg>Cerramientos</li>
      <li><svg class="service-icon" viewBox="0 0 42 42"><rect x="1" y="1" width="40" height="40" rx="4" fill="#c8322b" stroke="#fff" stroke-width="2"/><path d="M21 13 V29 M13 21 H29" fill="none" stroke="#fff" stroke-width="2.5"/></svg>Y mucho mas</li>
    </ul>
  </section>
  <div class="services-tab">NUESTROS SERVICIOS</div>

  <p class="hours">ABIERTO: LUNES - VIERNES 11:00 - 21:00 | SÁBADOS: 12:00 - 18:00 | DOMINGOS: CERRADO</p>

  <footer class="footer">
    presupuestos@ventalia-hogar.es | www.ventalia-hogar.es<br>
    Pol. Ind. Los Olmos, Nave 14, Alcobendas, Spain 28108
  </footer>
  <div class="call-pill">
    <span>LLÁMENOS AL</span>
    <svg viewBox="0 0 20 20" aria-hidden="true"><circle cx="10" cy="10" r="8.5" fill="none" stroke="#fff" stroke-width="1.6"/><path d="M7 5.5 L8.6 8 L7.6 9 Q8.6 11.4 11 12.4 L12 11.4 L14.5 13 L13.4 14.6 Q8.5 14.4 5.4 9.6 Q5.4 6.6 7 5.5 Z" fill="#fff"/></svg>
    <span>+34 611 24 57 93 para mas información</span>
  </div>

</main>
</body>
</html>
```